New home maintenance business, on the back of business card i would like dot points of my services provided.
these include,
General household repairs and maintenance
Painting
Verolin/Plaster Repairs
Fencing
Gardening and landscaping
Cleaning and removals
Doors and windows
Hinges and Locks
Fly screen/ screen door Repairs
I like black,silver, red but ill leav it up to you guys as something may be better for business.. , would also it be possible to create a logo for me incorporating the K&T as i want to make up t shirts in future thankyou
i would also like to put Marco Vintelli on the cards aswell please, and on back change painter to proffesional painter and decorator, please
i like alot of the designs sofar, i cant put my finger on wat 1 yet though!! cheers guys
Business
K&T HOME MAINTENANCE SERVICES
Lewis Vintelli 0467205184
kntmaintenance@postvale.com
ABN:57140328619

```html
<!DOCTYPE html>
<html lang="en">
<head>
<meta charset="utf-8">
<title>K&amp;T Home Maintenance Services – Business Card</title>
<link rel="stylesheet" href="https://fonts.googleapis.com/css2?family=Jost:wght@400;500&display=swap">
<style>
  :root {
    --page: #2b2b2b;
    --card-black: #1a1a1b;
    --card-red: #a8191e;
    --brand-red: #b3191f;
    --silver: #e9e9e9;
    --white: #ffffff;
    --ink: #1a1a1b;
  }
  * { margin: 0; padding: 0; box-sizing: border-box; }
  html, body {
    width: 1200px;
    height: 800px;
    overflow: hidden;
    background: var(--page);
  }
  .sheet {
    width: 1200px;
    height: 800px;
    display: flex;
    align-items: center;
    justify-content: center;
    gap: 40px;
  }
  .card {
    width: 540px;
    height: 309px;
    position: relative;
    box-shadow: 0 10px 30px rgba(0,0,0,.45);
    font-family: "Jost", "Century Gothic", sans-serif;
  }
  .card--front { background: var(--card-black); }
  .card--back { background: var(--card-red); }

  .business-name {
    position: absolute;
    left: 0;
    right: 0;
    display: flex;
    align-items: center;
    justify-content: center;
    gap: 12px;
  }
  .business-name__mark {
    width: 14px;
    height: 14px;
    flex: none;
  }
  .business-name__text {
    font-weight: 500;
    font-size: 20px;
    letter-spacing: 1.5px;
    text-transform: uppercase;
    white-space: nowrap;
  }
  .card--front .business-name { top: 92px; }
  .card--front .business-name__mark { background: var(--brand-red); }
  .card--front .business-name__text { color: var(--silver); }

  .card--back .business-name { top: 70px; }
  .card--back .business-name__mark { background: var(--ink); }
  .card--back .business-name__text { color: var(--white); }

  .contact {
    position: absolute;
    left: 0;
    right: 0;
    bottom: 44px;
    text-align: center;
  }
  .contact__person {
    color: var(--brand-red);
    font-weight: 500;
    font-size: 17px;
    letter-spacing: 1.5px;
    text-transform: uppercase;
    margin-bottom: 16px;
  }
  .contact__details {
    color: var(--silver);
    font-size: 14px;
    letter-spacing: 0.3px;
  }
  .contact__label { color: var(--brand-red); font-weight: 500; }

  .services {
    position: absolute;
    left: 0;
    right: 0;
    bottom: 50px;
    list-style: none;
    text-align: center;
    font-size: 12.5px;
    line-height: 1.6;
    letter-spacing: 0.6px;
    color: var(--silver);
    text-transform: uppercase;
  }
</style>
</head>
<body>
<main class="sheet">
  <section class="card card--front" aria-label="Business card front">
    <div class="business-name">
      <span class="business-name__mark"></span>
      <span class="business-name__text">K&amp;T Home Maintenance Services</span>
    </div>
    <div class="contact">
      <p class="contact__person">Lewis Vintelli</p>
      <p class="contact__details">
        <span class="contact__label">T:</span> 0467205184 ·
        <span class="contact__label">E:</span> kntmaintenance@postvale.com
      </p>
    </div>
  </section>

  <section class="card card--back" aria-label="Business card back">
    <div class="business-name">
      <span class="business-name__mark"></span>
      <span class="business-name__text">K&amp;T Home Maintenance Services</span>
    </div>
    <ul class="services">
      <li>General household repairs and maintenance · Painting</li>
      <li>Verolin / plaster repairs · Fencing · Gardening and landscaping</li>
      <li>Cleaning and removals · Doors and windows · Hinges and locks</li>
      <li>Fly screen / screen door repairs</li>
    </ul>
  </section>
</main>
</body>
</html>
```